Boutique Real Estate Brokerage Maplind Realty Website Design

Winning designer work on migrate as well through zip burrow.
We need a new website as an informational hub to aid our print and digital strategy as well as showing that we are located in Brooklyn and Florida. I have a boutique real estate brokerage and advisory firm specializing in residential leasing, multifamily sales and 1031 Exchange appropriation. This won't be a portal to search properties, it will be a place for information. I'd like space for an ebook to be downloaded and information on my probate sales and multifamily leasing marketing campaigns. I included my logo and will leave it up to the designer to come up with colors to match it. I have also attached verbiage for each page. The final design should have a modern high end look that reflects gentrifying Brooklyn as well as beautiful Florida.
Thank you!
Target Market(s)
Owners of income producing real estate and develop-able land in Brooklyn, NY and Florida.
Industry/Entity Type
Real Estate
Coding
Coded - Design and coding required
Number of Pages Required
5+ page
Colors
Designer to choose colors to be used in the design.
Requirements
Must have
- A modern elegant look
Nice to have
- pictures of brooklyn and florida
Should not have
- real estate search pages

```html
<!DOCTYPE html>
<html lang="en">
<head>
<meta charset="utf-8">
<title>Maplind Realty</title>
<link href="https://fonts.googleapis.com/css2?family=Playfair+Display:wght@400;700&family=Montserrat:wght@400;500;600&family=Open+Sans:wght@400;600&display=swap" rel="stylesheet">
<style>
:root{
  --pink:#ee1650;
  --navy:#23325a;
  --navy-dark:#1d2a4d;
  --white:#ffffff;
  --text:#555a66;
  --line:#d9dbe2;
  --quote-bg:#fdf8f8;
}
*{margin:0;padding:0;box-sizing:border-box}
html,body{width:1200px;height:2568px;overflow:hidden}
body{position:relative;background:var(--white);font-family:"Montserrat",sans-serif;color:var(--text)}
.abs{position:absolute}
/* top bar */
.topbar{top:0;left:0;width:1200px;height:31px;background:var(--pink);color:var(--white);font-size:12px}
.topbar .contact{left:112px;top:8px;display:flex;gap:26px}
.topbar .contact span{display:flex;align-items:center;gap:7px}
.social{display:flex;gap:10px}
.social i{display:block;width:14px;height:14px;border:1.5px solid currentColor;border-radius:3px}
.topbar .social{right:112px;top:8px}
/* nav */
.nav{top:31px;left:0;width:1200px;height:89px;background:var(--navy)}
.brand{display:flex;align-items:center;gap:10px;color:var(--white);font-family:"Montserrat",sans-serif;font-weight:600;font-size:14px;letter-spacing:1px;text-transform:uppercase}
.brand .mark{width:40px;height:40px;border-radius:50%;background:#9aa3b8}
.nav .brand{left:111px;top:24px}
.menu{left:466px;top:34px;display:flex;gap:24px;color:var(--white);font-size:13px;font-weight:500}
.menu .active{color:var(--pink)}
/* hero */
.hero{top:120px;left:0;width:1200px;height:480px}
.hero .left{left:0;top:0;width:610px;height:480px;background:linear-gradient(135deg,#6b4a3a,#3d2e26 55%,#5b6b3a)}
.hero .right{left:610px;top:0;width:590px;height:480px;background:linear-gradient(180deg,#6f8fb8 0%,#a98a7a 35%,#4f6a3e 55%,#3b4c5a 100%)}
.hero h1{left:0;top:186px;width:1200px;text-align:center;font-family:"Playfair Display",serif;font-weight:700;font-size:32px;line-height:40px;color:var(--white);text-shadow:0 2px 6px rgba(0,0,0,.5)}
.hero .arrow{top:210px;width:24px;height:24px;border:2px solid var(--white);border-radius:50%}
/* section titles */
.title{left:0;width:1200px;text-align:center;font-family:"Playfair Display",serif;font-size:29px;color:var(--navy)}
.title em{font-style:normal;color:var(--pink)}
.rule{left:517px;width:166px;height:2px;background:var(--line)}
.rule::after{content:"";position:absolute;left:58px;top:-2px;width:50px;height:5px;background:var(--navy)}
/* cards */
.glow{left:300px;top:700px;width:600px;height:460px;border-radius:50%;background:radial-gradient(closest-side,rgba(35,50,90,.13),rgba(35,50,90,0))}
.card{top:765px;width:296px;height:319px;background:var(--navy);color:var(--white)}
.card .photo{left:0;top:0;width:296px;height:219px}
.card .price{left:45px;top:210px;background:var(--pink);font-size:13px;font-weight:600;padding:5px 13px}
.card .doc{right:18px;top:190px;width:56px;height:56px;border-radius:50%;background:var(--navy);display:flex;align-items:center;justify-content:center}
.card h3{left:46px;top:245px;font-size:15px;font-weight:600}
.card .specs{left:46px;top:274px;display:flex;gap:12px}
.card .specs span{border:1px solid #8f98b3;border-radius:3px;font-size:10px;padding:6px 9px;display:flex;align-items:center;gap:7px}
.card.promo{background:var(--pink);display:flex;align-items:center;justify-content:center;text-align:center}
.card.promo p{font-size:13px;line-height:24px;padding:0 26px;margin-top:-60px}
/* about */
.about{top:1279px;left:0;width:1200px;height:318px}
.about .text{left:0;top:0;width:601px;height:318px;background:var(--navy);color:var(--white);font-size:13px;line-height:24px;padding:62px 40px 0 120px}
.about .photo{left:601px;top:0;width:599px;height:318px;background:linear-gradient(180deg,#7d8fb8 0%,#d8a892 40%,#2a4f86 65%,#1d2c4e 100%)}
/* testimonials */
.tcard{left:240px;top:1794px;width:720px;height:197px;background:var(--quote-bg);border:1px solid var(--line);font-family:"Open Sans",sans-serif;font-size:14px;line-height:25px;text-align:center;padding:58px 80px 0}
.qmark{left:575px;top:1770px;width:50px;height:50px;border-radius:50%;background:var(--white);border:1px solid var(--line);color:var(--pink);font-family:"Playfair Display",serif;font-size:34px;font-weight:700;text-align:center;line-height:60px}
.avatar{left:572px;top:1963px;width:56px;height:56px;border-radius:50%;background:linear-gradient(#c9d3e2,#5a6f92);border:3px solid var(--white)}
.tname{left:0;width:1200px;text-align:center;font-family:"Open Sans",sans-serif;font-size:12px;color:#333}
.dots{left:586px;top:2087px;display:flex;gap:8px}
.dots i{width:10px;height:10px;border-radius:50%;border:1.5px solid var(--pink)}
.dots i.on{background:var(--pink)}
/* skyline + footer */
.skyline{left:0;top:2003px;width:1200px;height:205px;background:linear-gradient(180deg,rgba(35,50,90,0) 0%,rgba(35,50,90,.35) 40%,var(--navy) 100%)}
.footer{left:0;top:2208px;width:1200px;height:360px;background:var(--navy);color:var(--white);font-family:"Open Sans",sans-serif;font-size:12px}
.footer h4{font-size:13px;font-weight:600;text-transform:uppercase;margin-bottom:26px}
.fcol{top:102px}
.fcol li{list-style:none;margin-bottom:8px}
.fcol .hl{color:var(--pink)}
.fcol .row{display:flex;gap:14px;margin-bottom:14px;line-height:17px}
.footer .brand{font-size:11px}
.footer .brand .mark{width:30px;height:30px}
.blurb{line-height:16px;width:190px;margin-top:22px}
.readmore{color:var(--pink);margin-top:20px;display:block}
.email{width:240px;height:36px;border:1px solid #b8bfd2;border-radius:18px;display:flex;align-items:center;justify-content:space-between;padding:0 22px;font-size:12px}
.fbar{left:0;top:305px;width:1200px;height:1px;background:#3b4a74}
.copy{left:124px;top:328px;font-size:10px;color:#c2c8d8}
.footer .social{right:122px;top:326px;gap:18px}
.footer .social i{width:16px;height:16px}
</style>
</head>
<body>

<div class="abs topbar">
  <div class="abs contact">
    <span><svg width="12" height="12" viewBox="0 0 24 24" fill="#fff"><path d="M6.6 10.8a15 15 0 006.6 6.6l2.2-2.2c.3-.3.7-.4 1-.2 1.1.4 2.3.6 3.6.6.6 0 1 .4 1 1V20c0 .6-.4 1-1 1A17 17 0 013 4c0-.6.4-1 1-1h3.5c.6 0 1 .4 1 1 0 1.3.2 2.5.6 3.6.1.3 0 .7-.2 1z"/></svg>1-888-555-0142</span>
    <span><svg width="13" height="10" viewBox="0 0 26 20" fill="none" stroke="#fff" stroke-width="2"><rect x="1" y="1" width="24" height="18"/><path d="M1 1l12 10L25 1"/></svg>hello@maplindrealty.com</span>
  </div>
  <div class="abs social"><i></i><i></i><i></i><i></i></div>
</div>

<header class="abs nav">
  <div class="abs brand"><span class="mark"></span>Maplind Realty</div>
  <nav class="abs menu">
    <span class="active">Home</span><span>About Us</span><span>Properties ⌄</span><span>Services</span><span>Agents ⌄</span><span>Membership</span><span>Contact Us</span>
  </nav>
</header>

<section class="abs hero">
  <div class="abs left" role="img" aria-label="Brooklyn brownstone row houses with stoops and railings"></div>
  <div class="abs right" role="img" aria-label="Florida apartment complex with palm trees beside a lake"></div>
  <h1 class="abs">Assisting landlords increase profits<br>while decreasing the stress.</h1>
  <span class="abs arrow" style="left:118px"></span>
  <span class="abs arrow" style="left:1058px"></span>
</section>

<h2 class="abs title" style="top:670px">How we <em>can help</em></h2>
<div class="abs rule" style="top:724px"></div>
<div class="abs glow"></div>

<article class="abs card" style="left:120px">
  <div class="abs photo" role="img" aria-label="Bright apartment interior with kitchen and dining table" style="background:linear-gradient(135deg,#e9ebe8,#b9bfc0 60%,#8a8a80)"></div>
  <span class="abs price">$240,000</span>
  <span class="abs doc"><svg width="16" height="20" viewBox="0 0 16 20" fill="none" stroke="#fff" stroke-width="1.6"><path d="M1 1h9l5 5v13H1z"/><path d="M4 10h8M4 13h8M4 16h6"/></svg></span>
  <h3 class="abs">Multi-Family Leasing</h3>
  <div class="abs specs"><span>⤢ 5000 Sq Ft</span><span>▭ 3 bed room</span></div>
</article>

<article class="abs card promo" style="left:452px">
  <p>We believe in our tenant selection process so much that we offer a Landlord Guarantee. Landlord guarantee we guarantee we place a good tenant in your unit or we'll refund our broker's fee.</p>
</article>

<article class="abs card" style="left:784px">
  <div class="abs photo" role="img" aria-label="Aerial view of a Florida town beside a river" style="background:linear-gradient(180deg,#b9cde0 0%,#8a9a8a 35%,#6e7b5e 70%,#4d5a44)"></div>
  <span class="abs price">$240,000</span>
  <span class="abs doc"><svg width="16" height="20" viewBox="0 0 16 20" fill="none" stroke="#fff" stroke-width="1.6"><path d="M1 1h9l5 5v13H1z"/><path d="M4 10h8M4 13h8M4 16h6"/></svg></span>
  <h3 class="abs">Site Selection Advisory</h3>
  <div class="abs specs"><span>⤢ 5000 Sq Ft</span><span>▭ 5 bed room</span></div>
</article>

<h2 class="abs title" style="top:1153px">About <em>Us</em></h2>
<div class="abs rule" style="top:1203px"></div>

<section class="abs about">
  <div class="abs text">Maplind Realty NYC-PB is a full-service real estate brokerage firm offices located Brooklyn, New York and West Palm Beach, Florida. Our firm focuses on multifamily leasing, sales and Commercial Real Estate Site Selection Advisory. Our clients are private and institutional multifamily real estate investors. Our team differentiates ourselves by our ability to investigate the highest and best use for real estate assets as well as our high deal closing rate.</div>
  <div class="abs photo" role="img" aria-label="City skyline at dusk with a blue bridge over the river"></div>
</section>

<h2 class="abs title" style="top:1684px">TESTI<em>MONIALS</em></h2>
<div class="abs rule" style="top:1734px"></div>

<div class="abs tcard">Lorem Ipsum is simply dummy text of the printing and typesetting industry. Lorem Ipsum has been industry's standard dummy text ever since the 1500s, when an printer took a galley of type and scrambled it to make a type specimen book.</div>
<div class="abs qmark">“</div>
<div class="abs avatar" role="img" aria-label="Portrait of the reviewer"></div>
<div class="abs tname" style="top:2029px">Aenean</div>
<div class="abs tname" style="top:2048px;color:#666">Estate Company</div>
<div class="abs dots"><i class="on"></i><i></i></div>

<div class="abs skyline" role="img" aria-label="City skyline silhouette"></div>

<footer class="abs footer">
  <div class="abs fcol" style="left:120px">
    <div class="brand"><span class="mark"></span>Maplind Realty</div>
    <p class="blurb">Lorem Ipsum is simply dummy text of the printing and typesetting industry.</p>
    <span class="readmore">Read More ›</span>
  </div>
  <div class="abs fcol" style="left:387px">
    <h4>Quick Links</h4>
    <ul><li class="hl">Home</li><li>About Us</li><li>Services</li><li>Membership</li></ul>
  </div>
  <div class="abs fcol" style="left:601px">
    <h4>Get In Touch</h4>
    <div class="row"><span>☎</span>1-888-555-0142</div>
    <div class="row"><span>✉</span>hello@maplindrealty.com</div>
    <div class="row"><span><svg width="10" height="14" viewBox="0 0 10 14" fill="none" stroke="#fff" stroke-width="1.4"><path d="M5 13S1 8 1 5a4 4 0 018 0c0 3-4 8-4 8z"/><circle cx="5" cy="5" r="1.5"/></svg></span><span>210 Harbor Lane<br>Blvd., P.O. Box 42,<br><span class="hl">Florida</span></span></div>
  </div>
  <div class="abs fcol" style="left:839px">
    <h4>Newsletter</h4>
    <div class="email">Enter Email <span>✉</span></div>
  </div>
  <div class="abs fbar"></div>
  <div class="abs copy">Copyright © 2019, Maplind Realty</div>
  <div class="abs social"><i></i><i></i><i></i><i></i></div>
</footer>

</body>
</html>
```